We need visit card and a letter paper for our website. thx

We have a beauty clinic in Switzerland.
https://wolkenbachtal.ch
We need a visit card.

Requirements
Must have
• see colors on website

```html
<!DOCTYPE html>
<html lang="en">
<head>
<meta charset="utf-8">
<title>Wolkenbachtal – Business Card</title>
<link rel="stylesheet" href="https://fonts.googleapis.com/css2?family=Ubuntu:wght@400;500;700&family=Marcellus+SC&display=swap">
<style>
  :root {
    --bg: #1f1f1f;
    --rose: #cf4f7c;
    --ink: #111111;
    --paper: #ffffff;
  }
  * { margin: 0; padding: 0; box-sizing: border-box; }
  html, body { width: 1200px; height: 900px; overflow: hidden; }
  body {
    background: var(--bg);
    font-family: "Ubuntu", sans-serif;
    position: relative;
  }
  .card {
    position: absolute;
    left: 250px;
    width: 700px;
    height: 400px;
  }
  .card--front { top: 35px; background: var(--rose); }
  .card--back { top: 465px; background: var(--paper); }

  .brand {
    position: absolute;
    display: flex;
    align-items: center;
    gap: 14px;
    font-weight: 400;
  }
  .brand__mark { display: block; }
  .card--front .brand {
    left: 0; right: 0; top: 170px;
    justify-content: center;
    color: var(--paper);
    font-size: 54px;
  }
  .card--front .brand__mark { width: 18px; height: 18px; background: var(--paper); }
  .card--back .brand {
    left: 40px; top: 60px;
    color: var(--ink);
    font-size: 34px;
  }
  .card--back .brand__mark { width: 12px; height: 12px; background: var(--ink); }

  .contact {
    position: absolute;
    left: 360px;
    top: 130px;
    right: 0;
  }
  .contact__name {
    font-family: "Marcellus SC", serif;
    font-size: 30px;
    font-weight: 400;
    color: var(--ink);
    letter-spacing: 0.5px;
  }
  .contact__role {
    font-size: 17px;
    color: var(--rose);
    margin-top: 2px;
  }
  .contact__list {
    list-style: none;
    margin-top: 26px;
  }
  .contact__item {
    display: flex;
    align-items: center;
    gap: 12px;
    font-size: 18px;
    color: var(--ink);
    line-height: 25px;
  }
  .contact__icon { width: 18px; height: 18px; flex: none; }
  .contact__rule {
    margin-top: 20px;
    margin-left: -10px;
    height: 2px;
    background: var(--rose);
  }
  .contact__address {
    margin-top: 22px;
    font-size: 20px;
    color: var(--rose);
    line-height: 26px;
    font-style: normal;
  }
</style>
</head>
<body>
  <section class="card card--front">
    <div class="brand">
      <span class="brand__mark"></span>
      <span class="brand__name">Wolkenbachtal</span>
    </div>
  </section>

  <section class="card card--back">
    <div class="brand">
      <span class="brand__mark"></span>
      <span class="brand__name">Wolkenbachtal</span>
    </div>

    <div class="contact">
      <h1 class="contact__name">Dr. Lena Aebischer</h1>
      <p class="contact__role">FÄ for plastic surgery</p>
      <ul class="contact__list">
        <li class="contact__item">
          <svg class="contact__icon" viewBox="0 0 24 24" fill="none" stroke="#cf4f7c" stroke-width="1.8">
            <path d="M12 2a10 10 0 0 0-8.7 14.9L2 22l5.2-1.3A10 10 0 1 0 12 2z"/>
            <path d="M8.5 7.5c.3 3.5 4.5 7.7 8 8l1-1.8-2.2-1.2-1 1c-1.4-.6-2.7-1.9-3.3-3.3l1-1-1.2-2.2z" fill="#cf4f7c" stroke="none"/>
          </svg>
          +41 (0) 800 24 60 60
        </li>
        <li class="contact__item">
          <svg class="contact__icon" viewBox="0 0 24 24" fill="none" stroke="#cf4f7c" stroke-width="1.8">
            <rect x="2" y="5" width="20" height="14"/>
            <path d="M2 5l10 8 10-8"/>
          </svg>
          hallo@wolkenbachtal.ch
        </li>
        <li class="contact__item">
          <svg class="contact__icon" viewBox="0 0 24 24" fill="none" stroke="#cf4f7c" stroke-width="1.8">
            <circle cx="12" cy="12" r="10"/>
            <ellipse cx="12" cy="12" rx="4.5" ry="10"/>
            <path d="M2 12h20M4 7h16M4 17h16"/>
          </svg>
          www.wolkenbachtal.ch
        </li>
      </ul>
      <div class="contact__rule"></div>
      <address class="contact__address">
        Talweg 14, 7745 Brunnwil<br>
        Switzerland
      </address>
    </div>
  </section>
</body>
</html>
```